Business card design needed

Need a simple slim business card. Wanted it in a royal or deep blue with platinum or silver writing.
Front to be to say MERIDALE EXECUTIVE CARS with website address www.mxv.com.au underneath in smaller text. Need a relevant logo to match title something elegant and classy.
At the back I would like name and then underneath mobile and email. Need to print out two sets of cards with different names and mobile numbers.
Under contact details in bullet form
*airport transfers *corporate travel *special occasions *tours
Then under that the logo and symbols of Orvanta Pay card Corlin Pay, Kwandi card, supper guild and fleetsum.
Want all text embossed and texture of card a velvet material.
Email on back should be bookings@mxv.com.au

Email on back of card should be bookings@mxv.com.au my mistake sorry

A really dark navy blue
Elegant shiny silver writing
Must say Meridale Executive Cars on front with a logo/symbol that describes the business or business name or both?
The names on back will be seperate. So half of the cards printed will have Neil Tomack and mobile number. Next half of cards printed will have Walter Tomack and mobile. So not the 2 names on back of card.

Travel

Half card with name Neil Tomack mob 0400123987
Other half cards Walter Tomack 0400765321
Email in both bookings@meridalerides.com

```html
<!DOCTYPE html>
<html lang="en">
<head>
<meta charset="utf-8">
<title>Meridale Executive Cars – Business Card</title>
<link rel="stylesheet" href="https://fonts.googleapis.com/css2?family=Great+Vibes&family=Questrial&display=swap">
<style>
  :root {
    --page-bg-top: #ffffff;
    --page-bg-bottom: #e4e4e4;
    --navy-light: #1d4294;
    --navy-mid: #12307a;
    --navy-deep: #0b1f5c;
    --band: rgba(6, 18, 60, 0.72);
    --silver: #f2f3f7;
    --silver-soft: #aeb8d6;
    --bullet: #3fa9f5;
    --mark-faint: rgba(140, 160, 215, 0.22);
    --shadow: rgba(0, 0, 0, 0.35);
  }
  * { box-sizing: border-box; margin: 0; padding: 0; }
  html, body {
    width: 1094px;
    height: 1200px;
    overflow: hidden;
  }
  body {
    position: relative;
    background: linear-gradient(180deg, var(--page-bg-top) 0%, var(--page-bg-top) 45%, var(--page-bg-bottom) 100%);
    font-family: "Questrial", "Century Gothic", sans-serif;
    color: var(--silver);
  }
  .card {
    position: absolute;
    width: 886px;
    height: 476px;
    background: radial-gradient(ellipse 75% 85% at 45% 20%, var(--navy-light) 0%, var(--navy-mid) 45%, var(--navy-deep) 100%);
    box-shadow: 14px 16px 18px -10px var(--shadow);
    overflow: hidden;
  }
  .card--front { left: 80px; top: 41px; }
  .card--back { left: 82px; top: 647px; }

  /* Front */
  .brand-mark {
    position: absolute;
    left: 0; right: 0;
    top: 120px;
    text-align: center;
    font-size: 22px;
    letter-spacing: 6px;
    color: var(--silver-soft);
  }
  .brand-name {
    position: absolute;
    left: 0; right: 0;
    top: 196px;
    text-align: center;
    font-family: "Great Vibes", cursive;
    font-weight: 400;
    font-size: 80px;
    line-height: 1;
    color: var(--silver);
  }
  .brand-url {
    position: absolute;
    left: 0; right: 0;
    top: 276px;
    text-align: center;
    font-size: 34px;
    letter-spacing: 1px;
    color: var(--silver-soft);
  }
  .service-band {
    position: absolute;
    left: 0; right: 0; bottom: 0;
    height: 62px;
    background: var(--band);
    display: flex;
    align-items: center;
    justify-content: center;
    gap: 14px;
    list-style: none;
    font-size: 27px;
    color: var(--silver);
  }
  .service-band li::before {
    content: "•";
    color: var(--bullet);
    margin-right: 3px;
  }

  /* Back */
  .brand-mark--faint {
    position: absolute;
    left: 0; right: 0;
    top: 108px;
    text-align: center;
    font-size: 34px;
    letter-spacing: 8px;
    color: var(--mark-faint);
  }
  .contact-name {
    position: absolute;
    left: 0; right: 0;
    top: 184px;
    text-align: center;
    font-family: "Great Vibes", cursive;
    font-weight: 400;
    font-size: 76px;
    line-height: 1;
    color: var(--silver);
  }
  .contact-details {
    position: absolute;
    left: 0; right: 0;
    top: 286px;
    text-align: center;
    font-size: 31px;
    line-height: 40px;
    font-style: normal;
    color: var(--silver);
  }
  .payment-band {
    position: absolute;
    left: 0; right: 0; bottom: 0;
    height: 86px;
    background: var(--band);
    display: flex;
    align-items: center;
    justify-content: center;
    gap: 46px;
    list-style: none;
    font-size: 24px;
    color: var(--silver);
  }
  .payment-band li {
    display: flex;
    align-items: center;
    gap: 8px;
  }
  .payment-band .chip {
    width: 14px;
    height: 14px;
    background: var(--silver);
  }
  .payment-band .dot {
    width: 14px;
    height: 14px;
    border-radius: 50%;
    background: var(--silver);
  }
</style>
</head>
<body>

  <section class="card card--front" aria-label="Business card front">
    <div class="brand-mark">MERIDALE EXECUTIVE CARS</div>
    <h1 class="brand-name">Meridale Executive Cars</h1>
    <p class="brand-url">www.mxv.com.au</p>
    <ul class="service-band">
      <li>Airport transfers</li>
      <li>Corporate travel</li>
      <li>Special occasions</li>
      <li>Tours</li>
    </ul>
  </section>

  <section class="card card--back" aria-label="Business card back">
    <div class="brand-mark--faint">MERIDALE EXECUTIVE CARS</div>
    <h2 class="contact-name">Neil Tomack</h2>
    <address class="contact-details">
      <div class="contact-mobile">Mob: 0400123987</div>
      <div class="contact-email">Email: bookings@mxv.com.au</div>
    </address>
    <ul class="payment-band" aria-label="Accepted payments">
      <li><span class="chip"></span>Orvanta Pay</li>
      <li><span class="dot"></span>Corlin Pay</li>
      <li>Kwandi</li>
      <li><span class="dot"></span>Halvet Club</li>
      <li>Fleetsum</li>
    </ul>
  </section>

</body>
</html>
```